VELTRIX Web Page

We need a corporate web site for a new company VELTRIX Corporation. VELTRIX is a technology company that has developed a new virtualization solution for corporate applications. Our target customers are IT professionals. We have a logo, which we will provide.

Final design should communicate: innovation, stability, professionalism

Industry/Entity Type

It Company

```html
<!DOCTYPE html>
<html lang="en">
<head>
<meta charset="utf-8">
<title>VELTRIX — Virtualization for Corporate Applications</title>
<link href="https://fonts.googleapis.com/css2?family=Bebas+Neue&family=Arimo:wght@400;700&display=swap" rel="stylesheet">
<style>
:root{
  --orange:#c84b27;
  --orange-dark:#a83a1c;
  --navy:#2e3a4f;
  --navy-dark:#222b3b;
  --cyan:#1ea5d4;
  --paper:#f3efe6;
  --map:#e4e4e4;
  --ink:#1d1d1f;
  --white:#ffffff;
}
*{margin:0;padding:0;box-sizing:border-box}
html,body{width:1200px;height:925px;overflow:hidden}
body{position:relative;background:var(--paper);font-family:"Arimo",Arial,sans-serif;color:var(--ink)}
.abs{position:absolute}
.top-band{left:0;top:0;width:1200px;height:57px;background:var(--orange)}
.hero-bg{left:0;top:57px;width:1200px;height:352px;background:var(--map)}
.footer-bg{left:0;top:830px;width:1200px;height:95px;background:var(--map)}
header{position:relative;z-index:5}
.logo-tab{left:166px;top:0;width:272px;height:62px;background:var(--map);border-right:5px solid var(--navy-dark);border-bottom:4px solid var(--navy-dark)}
.brand{font-family:"Bebas Neue",sans-serif;color:var(--ink);letter-spacing:2px;line-height:1}
.logo-tab .brand{position:absolute;left:26px;top:14px;font-size:48px}
.utility{left:772px;top:21px;font-size:11px;color:var(--white)}
.utility a{color:var(--white);text-decoration:none}
.login{left:881px;top:17px;width:99px;height:23px;border-radius:12px;background:var(--white);font-size:11px;line-height:23px;text-align:center;color:var(--ink)}
.nav{left:439px;top:57px;display:flex;height:73px}
.nav a{font-family:"Bebas Neue",sans-serif;font-size:27px;color:var(--navy-dark);text-decoration:none;line-height:73px;padding:0 22px}
.nav a.active{background:var(--orange);color:var(--white);width:99px;text-align:center;padding:0}
.art-team{left:222px;top:134px;width:416px;height:275px;background:linear-gradient(180deg,#d6dde3 0%,#8a97aa 45%,#34415a 100%)}
.art-devices{left:640px;top:134px;width:382px;height:286px;background:linear-gradient(90deg,#dcdfe3 0%,#c9d3dc 45%,#7fa9cc 75%,#b8d0e2 100%)}
.headline{font-family:"Bebas Neue",sans-serif;line-height:1}
.h1{left:211px;top:417px;font-size:39px;color:var(--navy)}
.h2{left:288px;top:455px;font-size:50px;color:var(--orange);white-space:nowrap}
.h2 span{color:var(--cyan)}
.h3{left:730px;top:499px;font-size:50px;color:var(--cyan)}
.card{position:absolute;width:211px;color:var(--white);border-bottom:7px solid rgba(0,0,0,.28)}
.card.orange{background:var(--orange)}
.card.navy{background:var(--navy)}
.card .icon{position:absolute;left:52px;width:107px;height:107px;border-radius:50%;background:var(--cyan);display:flex;align-items:center;justify-content:center}
.card h2{position:absolute;left:0;width:100%;text-align:center;font-family:"Bebas Neue",sans-serif;font-weight:400;font-size:31px}
.card p,.card ul{position:absolute;left:18px;right:14px;font-size:11px;line-height:16px}
.card ul{list-style:none}
.card li{border-bottom:1px solid rgba(255,255,255,.18);padding:3px 0 4px}
.card li:last-child{border:0}
.ribbon{position:absolute;right:3px;top:0;width:19px;height:46px;background:var(--navy-dark)}
.card.navy .ribbon{background:#1b2230}
.ribbon span{position:absolute;left:1px;top:30px;transform:rotate(-90deg);transform-origin:left top;font-family:"Bebas Neue",sans-serif;font-size:13px;color:var(--white)}
.copyright{left:160px;top:852px;font-size:11px;color:#333}
.copyright a{color:var(--orange);text-decoration:none;margin-left:8px}
.social{left:509px;top:848px;display:flex;gap:3px}
.social i{width:21px;height:21px;border-radius:50%;background:#6a6d73;display:block}
.phone{left:630px;top:838px;display:flex;align-items:center;gap:3px;font-family:"Bebas Neue",sans-serif;font-size:38px;color:var(--orange)}
.footer-brand{left:858px;top:840px;font-size:38px}
</style>
</head>
<body>
<div class="abs top-band"></div>
<div class="abs hero-bg"></div>
<div class="abs footer-bg"></div>

<div class="abs art-team" role="img" aria-label="Illustration of silhouetted people lifting a blue puzzle piece onto stacked navy puzzle blocks"></div>
<div class="abs art-devices" role="img" aria-label="Two smartphones showing a task list and map app in front of a blue globe"></div>

<header>
  <div class="abs logo-tab"><div class="brand">VELTRIX</div></div>
  <div class="abs utility"><a href="#">FAQs</a> &nbsp;|&nbsp; <a href="#">Apply Now</a></div>
  <div class="abs login">Customer Login</div>
  <nav class="abs nav">
    <a class="active" href="#">Home</a>
    <a href="#">About</a>
    <a href="#">Services</a>
    <a href="#">Partners</a>
    <a href="#">Contact</a>
  </nav>
</header>

<div class="abs headline h1">We developed a better way to deliver</div>
<div class="abs headline h2">Virtualization solution <span>for corporate</span></div>
<div class="abs headline h3">Applications</div>

<section>
  <article class="card orange" style="left:159px;top:606px;height:180px">
    <div class="icon" style="top:-63px">
      <svg width="48" height="40" viewBox="0 0 48 40"><rect x="16" y="1" width="16" height="8" rx="2" fill="none" stroke="#fff" stroke-width="3"/><rect x="1" y="8" width="46" height="31" rx="4" fill="#fff"/><rect x="21" y="18" width="6" height="7" fill="none" stroke="#1ea5d4" stroke-width="2"/><line x1="1" y1="21" x2="47" y2="21" stroke="#1ea5d4" stroke-width="2"/></svg>
    </div>
    <div class="ribbon"><span>MORE</span></div>
    <h2 style="top:51px">What we do</h2>
    <p style="top:99px">Lorem ipsum dolor sit amet, consectetuer adipiscing elit, sed diam nonummy nibh euismod tincidunt ut laoreet dolore magna</p>
  </article>

  <article class="card navy" style="left:374px;top:564px;height:222px">
    <div class="icon" style="top:-47px">
      <svg width="54" height="44" viewBox="0 0 54 44"><path d="M4 30 L40 4 L48 30 Z" fill="#fff"/><rect x="1" y="26" width="10" height="8" fill="#fff" transform="rotate(-30 6 30)"/><path d="M16 32 q2 10 12 6" fill="none" stroke="#fff" stroke-width="3"/></svg>
    </div>
    <div class="ribbon"><span>MORE</span></div>
    <h2 style="top:93px">Who we are</h2>
    <p style="top:141px">Lorem ipsum dolor sit amet, consectetuer adipiscing elit, sed diam nonummy nibh euismod tincidunt ut laoreet</p>
  </article>

  <article class="card orange" style="left:589px;top:600px;height:186px">
    <div class="icon" style="top:-57px">
      <svg width="54" height="46" viewBox="0 0 54 46"><path d="M1 45 V26 L16 12 L30 26 L52 4 V45 Z" fill="#fff"/><path d="M1 38 L16 26 L30 36 L52 20" fill="none" stroke="#1ea5d4" stroke-width="3"/></svg>
    </div>
    <div class="ribbon"><span>MORE</span></div>
    <h2 style="top:57px">What we offer</h2>
    <ul style="top:102px"><li>Lorem ipsum dolor sit amet,</li><li>Consectetuer adipiscing elit, sed</li><li>Diam nonummy nibh euismod</li></ul>
  </article>

  <article class="card navy" style="left:806px;top:577px;height:209px">
    <div class="icon" style="top:-34px">
      <svg width="52" height="52" viewBox="0 0 52 52"><path d="M3 3 V49 H49" fill="none" stroke="#fff" stroke-width="2"/><path d="M12 40 L38 14" stroke="#fff" stroke-width="6"/><path d="M26 8 H44 V26 Z" fill="#fff"/></svg>
    </div>
    <div class="ribbon"><span>MORE</span></div>
    <h2 style="top:79px">Where we have been</h2>
    <ul style="top:125px"><li>Lorem ipsum dolor sit amet,</li><li>Consectetuer adipiscing elit, sed</li><li>Diam nonummy nibh euismod</li></ul>
  </article>
</section>

<footer>
  <div class="abs copyright">Copyright © 2013 veltrix.example &nbsp;All rights reserved. <a href="#">Privacy Policy</a></div>
  <div class="abs social" aria-label="Social links"><i></i><i></i><i></i><i></i></div>
  <div class="abs phone">
    <svg width="14" height="18" viewBox="0 0 14 18"><path d="M3 1 L6 5 L4 7 Q6 11 9 13 L11 11 L14 14 L11 17 Q2 14 0 4 Z" fill="#666"/></svg>
    (800) 555 0142
  </div>
  <div class="abs brand footer-brand">VELTRIX</div>
</footer>
</body>
</html>
```